Design a powerpoint background using company logo/colours

We require a powerpoint background that incorporates our company colours and logo. I have attached the logo in various sizes.

Have fun and be imaginative

Our company colours are white and Red-236, Green-22 and Blue 86.
Please use these colours in designing the ppt background

Industry/Entity Type

It Company

Colors

Designer to choose colors to be used in the design.

```html
<!DOCTYPE html>
<html lang="en">
<head>
<meta charset="utf-8">
<title>Nexora slide background</title>
<link rel="stylesheet" href="https://fonts.googleapis.com/css2?family=Antonio:wght@300;600&display=swap">
<style>
  :root {
    --brand: #ec1656;
    --brand-deep: #d50f4b;
    --brand-mid: #ee3a6c;
    --brand-light: #f2668f;
    --brand-pale: #f58aa9;
    --paper: #ffffff;
    --ink: #111111;
    --rim: #d9d9d9;
  }
  html, body {
    margin: 0;
    padding: 0;
    width: 1200px;
    height: 900px;
    overflow: hidden;
    background: var(--paper);
  }
  .slide {
    position: relative;
    width: 1200px;
    height: 900px;
    overflow: hidden;
    background: var(--paper);
  }
  .slide-frame {
    position: absolute;
    inset: 0;
    width: 1200px;
    height: 900px;
  }
  .brand-lockup {
    position: absolute;
    top: 26px;
    left: 0;
    width: 1200px;
    display: flex;
    justify-content: center;
    align-items: center;
    gap: 14px;
  }
  .brand-name {
    font-family: "Antonio", "Arial Narrow", sans-serif;
    font-weight: 600;
    font-size: 64px;
    line-height: 1;
    letter-spacing: 2px;
    color: var(--brand);
  }
  .brand-square {
    width: 40px;
    height: 40px;
    background: var(--brand);
  }
  .resolution-label {
    position: absolute;
    top: 370px;
    left: 0;
    width: 1200px;
    margin: 0;
    text-align: center;
    font-family: "Antonio", "Arial Narrow", sans-serif;
    font-weight: 300;
    font-size: 158px;
    line-height: 1;
    letter-spacing: 14px;
    color: var(--ink);
  }
</style>
</head>
<body>
<main class="slide">
  <svg class="slide-frame" viewBox="0 0 1200 900" aria-hidden="true">
    <!-- left ray fan -->
    <g class="ray-fan ray-fan--left">
      <polygon points="0,0 380,0 350,62 0,276" fill="var(--brand)"/>
      <polygon points="0,0 380,0 0,60" fill="var(--brand-pale)"/>
      <polygon points="0,78 380,0 0,128" fill="var(--brand-light)"/>
      <polygon points="0,150 380,0 0,196" fill="var(--brand-mid)"/>
      <polygon points="0,254 350,62 355,78 0,276" fill="var(--brand-deep)"/>
    </g>
    <!-- right ray fan -->
    <g class="ray-fan ray-fan--right">
      <polygon points="1200,0 820,0 850,62 1200,286" fill="var(--brand)"/>
      <polygon points="1200,0 820,0 1200,60" fill="var(--brand-pale)"/>
      <polygon points="1200,78 820,0 1200,128" fill="var(--brand-light)"/>
      <polygon points="1200,150 820,0 1200,196" fill="var(--brand-mid)"/>
      <polygon points="1200,264 850,62 845,78 1200,286" fill="var(--brand-deep)"/>
    </g>
    <!-- header disc -->
    <circle class="header-disc" cx="600" cy="-78" r="258" fill="var(--paper)" stroke="var(--rim)" stroke-width="3"/>
    <!-- footer band -->
    <rect class="footer-band" x="0" y="810" width="1200" height="90" fill="var(--brand)"/>
    <!-- footer marker -->
    <rect class="footer-marker" x="574" y="776" width="52" height="52" fill="var(--paper)" stroke="var(--brand)" stroke-width="4"/>
  </svg>

  <header class="brand-lockup">
    <span class="brand-name">Nexora</span>
    <span class="brand-square"></span>
  </header>

  <h1 class="resolution-label">1024x768:96dpi</h1>
</main>
</body>
</html>
```